63Crest Web Design Project

We need a new web site for our company. 63Crest provides a range of location intelligence and marketing services to assist clients in improving their performance. On the location intelligence side we're the local partner for Vorqel Plin (Quill and Lumen) in South Africa, we're the local reseller and can assist company with the implementation and customization - we'll shortly receive the Vorqel partner logo that should also be displayed on the Homepage. On the marketing side, we provide a range of marketing services for example Tenders, Event Management and Copy writing. The company is a blend between a mapping and marketing services company. You can have a look at the existing site at www.63crest.co.za
Updates

Dear designers, the budget for my project has been increased to $700. Looking forward to receiving your designs. Kind regards Tobias

Dear designers - many thanks for all the great designs received to date. We'll provide feedback shortly. Kind regards 63Crest

Target Market(s)

Our target market is public and private organisations, and online customers (those with a web presence) primarily in South Africa

Industry/Entity Type

Marketing

Requirements
Must have
• I have uploaded the latest text and suggested pages at this stage. Important is that it should be easy to edit the pages in an HTML editor, e.g. Frontpage. I suspect that the navigation will be expanded later e.g. careers, success stories - so it should be easy for me add new sections to the navigation later on. I have also uploaded the different 63Crest logo designs. Please include links on the Homepage for Terms and Conditions and PAIA - see www.63crest.co.za - also the Copyright Note at the bottom of every page
Nice to have
• Although we're targeting corporates and government, and online customers, the site should be fresh and easy to navigate. I like the use of photographs on sites and make them look more interesting than simply text. Although we're also providing marketing services, the location intelligence (mapping) and Vorqel Quill/Lumen aspect are perhaps the most important part of the website.

```html
<!DOCTYPE html>
<html lang="en">
<head>
<meta charset="utf-8">
<title>63Crest – Map Office</title>
<link rel="stylesheet" href="https://fonts.googleapis.com/css2?family=Ubuntu:wght@500;700&family=Arimo:wght@400;700&display=swap">
<style>
:root{
  --header-top:#5d636b;
  --header-bottom:#3f454c;
  --nav-divider:#6b7179;
  --accent:#e31b23;
  --accent-dark:#b5121a;
  --panel:#ffffff;
  --page:#ffffff;
  --title:#5b5e62;
  --body:#6d7074;
  --rule:#d6d8da;
  --dark-btn:#4b5158;
  --light-btn:#cfd1d3;
}
*{margin:0;padding:0;box-sizing:border-box}
html,body{width:1200px;height:750px;overflow:hidden;background:var(--page);font-family:"Arimo",Arial,sans-serif;color:var(--body)}
.site{position:relative;width:1200px;height:750px}
.abs{position:absolute}

/* header */
.masthead{left:166px;top:0;width:870px;height:117px;background:linear-gradient(var(--header-top),var(--header-bottom))}
.brand{left:52px;top:40px;display:flex;align-items:center;gap:8px;font-family:"Ubuntu",sans-serif;font-weight:700;font-size:26px;color:#fff}
.brand-dot{width:14px;height:14px;border-radius:50%;background:#fff}
.nav{left:199px;top:0;height:117px;display:flex;list-style:none}
.nav li{height:117px;border-left:1px solid var(--nav-divider);display:flex;align-items:center;justify-content:center;font-family:"Ubuntu",sans-serif;font-weight:500;font-size:12.5px;color:#fff;padding-top:10px}
.nav li.current{background:var(--accent)}
.nav li.current span{border-bottom:1px solid #fff}
.nav li:last-child{border-right:1px solid var(--nav-divider)}

/* panels */
.news-panel{left:166px;top:117px;width:268px;height:227px;background:var(--panel);box-shadow:0 3px 6px rgba(0,0,0,.12)}
.about-panel{left:769px;top:117px;width:267px;height:229px;background:var(--panel);box-shadow:0 3px 6px rgba(0,0,0,.12)}
.double-rule{height:3px;border-top:1px solid var(--rule);border-bottom:1px solid var(--rule)}
.section-title{font-family:"Arimo",sans-serif;font-weight:700;font-size:14px;color:var(--title);display:flex;align-items:center;gap:8px}
.news-card{left:27px;width:200px;height:55px;border-radius:6px;box-shadow:0 2px 4px rgba(0,0,0,.25);overflow:hidden}
.news-card.first{top:61px;background:linear-gradient(#6d95b0,#3c6f8e)}
.news-card.second{top:137px;background:linear-gradient(100deg,#bcd6ea 0%,#d8e6f0 40%,#f0a93a 55%,#e9d7c9 75%,#a9c5dc 100%)}
.news-card .headline{position:absolute;left:21px;top:9px;font-family:"Ubuntu",sans-serif;font-weight:500;font-size:13.5px;color:#fff}
.news-card .date{position:absolute;right:18px;top:37px;font-size:8px;font-style:italic;color:#fff}
.pill{height:19px;border-radius:10px;font-size:10px;display:flex;align-items:center;justify-content:center}
.archive{left:97px;top:202px;width:59px;background:linear-gradient(#e2e3e4,#bfc1c3);color:#fff}
.more{left:100px;top:202px;width:59px;background:linear-gradient(#636970,#41464c);color:#cfd2d5}
.about-text{left:30px;top:57px;width:210px;font-size:9px;line-height:15px}

.hero{left:434px;top:117px;width:335px;height:401px;background:linear-gradient(160deg,#eef0f0 0%,#c9ccc9 35%,#3a3a3e 60%,#1f2024 100%)}

/* partners */
.partner-badge{left:197px;top:398px;width:69px;height:70px;background:linear-gradient(#e9f2fb,#cfe2f5);border:1px solid #8fb6de}
.partner-mark{left:300px;top:420px;width:92px;height:26px;border-radius:13px;background:#dfe3e8}
.slider-controls{left:401px;top:479px;width:88px;height:31px;border-radius:16px;background:linear-gradient(var(--accent),var(--accent-dark));display:flex}
.slider-controls span{flex:1;display:flex;align-items:center;justify-content:center}
.slider-controls span:first-child{border-right:1px solid #c4141c}

/* testimonials */
.notebook{left:769px;top:346px;width:52px;height:80px;background:linear-gradient(135deg,#e9eaeb,#fafafa 60%,#fff);clip-path:polygon(0 0,100% 0,0 100%)}
.avatar{left:790px;top:392px;width:65px;height:62px;border-radius:8px;border:1px solid #d3d5d7;background:linear-gradient(#dfe6ee,#4f6a87)}
.person-name{left:790px;top:461px;width:66px;text-align:center;font-size:8.5px;font-weight:700;color:var(--accent)}
.person-role{left:790px;top:474px;width:66px;text-align:center;font-size:8px;font-weight:700;color:#555}
.quote{left:870px;top:413px;width:160px;font-size:9px;line-height:15px}
.quote-mark{font-family:Georgia,serif;font-size:30px;color:#c3c5c7;font-weight:700}
.pager{left:790px;top:495px;display:flex;list-style:none;font-size:8.5px}
.pager li{width:18px;height:28px;display:flex;align-items:center;justify-content:center}
.pager li.active{background:var(--accent);color:#fff}

/* footer */
.footer-rule{left:165px;top:518px;width:872px;border-top:1px solid #c9cbcd}
.region-shape{left:167px;top:518px;width:104px;height:69px;background:#e2e3e4;border-radius:0 0 40px 55px}
.footer-links{left:283px;top:543px;display:flex;list-style:none;font-size:9px;color:#777}
.footer-links li+li::before{content:"|";margin:0 11px}
.copyright{right:168px;top:543px;font-size:9px;color:#777}
</style>
</head>
<body>
<div class="site">

  <header class="masthead abs">
    <div class="brand abs"><span class="brand-dot"></span>63Crest</div>
    <ul class="nav abs">
      <li style="width:68px">Home</li>
      <li class="current" style="width:93px"><span>Map Office</span></li>
      <li style="width:107px">Tender Office</li>
      <li style="width:100px">Sales Office</li>
      <li style="width:112px">Content Office</li>
      <li style="width:98px">Event Office</li>
      <li style="width:93px">Contact Us</li>
    </ul>
  </header>

  <section class="news-panel abs">
    <div class="double-rule abs" style="left:19px;top:20px;width:218px"></div>
    <h2 class="section-title abs" style="left:27px;top:32px">News
      <svg width="16" height="8" viewBox="0 0 16 8"><path d="M0 4h14M10 1l4 3-4 3" fill="none" stroke="#9a9da0" stroke-width="1"/></svg></h2>
    <article class="news-card first abs" role="img" aria-label="Photo of a man working on a laptop beside the sea">
      <span class="headline">Luxury Event in Monaco</span>
      <span class="date">23 Febuary 2012r.</span>
    </article>
    <article class="news-card second abs" role="img" aria-label="Photo of a child with an orange sail against blue sky"></article>
    <div class="double-rule abs" style="left:19px;top:210px;width:218px"></div>
    <div class="pill archive abs">Archive</div>
  </section>

  <div class="hero abs" role="img" aria-label="Photo of a smiling business team in suits"></div>

  <section class="about-panel abs">
    <div class="double-rule abs" style="left:22px;top:20px;width:218px"></div>
    <h2 class="section-title abs" style="left:30px;top:33px">What We do ?
      <svg width="16" height="8" viewBox="0 0 16 8"><path d="M0 4h14M10 1l4 3-4 3" fill="none" stroke="#9a9da0" stroke-width="1"/></svg></h2>
    <p class="about-text abs">Lorem ipsum dolor sit amet, consectetur adipisic-ing elit, sed do eiusmod tempor incididunt ut labore et dolore magna aliqua. Ut enim ad minim veniam, quis nostrud exercitation ullamco laboris nisi ut aliquip ex ea commodo consequat. Duis aute irure dolor in reprehenderit in voluptate velit esse cillum dolore eu fugiat nulla pariatur. Excepteur sint occaecat cupidatat non proident, sunt in culpa qui officia deserunt mollit anim id est</p>
    <div class="double-rule abs" style="left:22px;top:210px;width:218px"></div>
    <div class="pill more abs">More</div>
  </section>

  <h2 class="section-title abs" style="left:193px;top:358px">Partners</h2>
  <div class="partner-badge abs" role="img" aria-label="Authorized reseller partner badge"></div>
  <div class="partner-mark abs" role="img" aria-label="Vorqel partner mark"></div>

  <div class="slider-controls abs">
    <span><svg width="22" height="10" viewBox="0 0 22 10"><path d="M22 5H2M6 1L2 5l4 4" fill="none" stroke="#fff" stroke-width="1.3"/></svg></span>
    <span><svg width="22" height="10" viewBox="0 0 22 10"><path d="M0 5h20M16 1l4 4-4 4" fill="none" stroke="#fff" stroke-width="1.3"/></svg></span>
  </div>

  <div class="notebook abs" role="img" aria-label="Notebook and pen"></div>
  <h2 class="section-title abs" style="left:798px;top:358px">Testimonials</h2>
  <div class="avatar abs" role="img" aria-label="Portrait of the client"></div>
  <div class="person-name abs">Daniel Reeve</div>
  <div class="person-role abs">Norvane CEO</div>
  <div class="quote-mark abs" style="left:868px;top:382px">“</div>
  <p class="quote abs">But I must explain to you how all this mistaken idea of denouncing pleasure and praising pain was born and I will give you a complete !</p>
  <div class="quote-mark abs" style="left:1005px;top:452px">”</div>
  <ul class="pager abs">
    <li>1</li><li>2</li><li class="active">3</li><li>4</li><li>5</li>
  </ul>

  <footer>
    <div class="region-shape abs" role="img" aria-label="Map outline of South Africa"></div>
    <div class="footer-rule abs"></div>
    <ul class="footer-links abs">
      <li>Terms and Conditions</li><li>PAIA</li><li>Caarers</li><li>Contact Us</li>
    </ul>
    <p class="copyright abs">Copyright © 2012 by 63Crest. All Rights Reserved</p>
  </footer>

</div>
</body>
</html>
```